Website Design - for Energy Efficiency company - large corporate feel

Hi there,
Thanks for checking out this project!
We're a UK based energy efficiency business. We arrange for energy efficient systems to be fitted in people's houses (i.e. efficient boilers, solar panels etc.) However, we do not install them ourselves as we have accredited installers who install on our behalf. Therefore the website should appeal to these businesses and have a very professional corporate feel. The final design should communicate that we are a financially safe large corporation.
Our existing website should not be used for inspiration as the style and content are very outdated (it was from a time when were installers - which we no longer are).
The new website design should use the greens from our logo, however I don't want the site saturated in this colour.
I'm really open to your chosen layout and therefore I'm not a huge fan of including links to websites I like - as I don't want to limit your own creativity. However, I would like it to look corporate (but not too boring and unimaginative).
So here's a few links to websites that I feel give a feel of financially safe / large corporate etc. Although you certainly don't have to design with this style / layout in mind:
http://www.brelvanhub.org.uk/advice
http://www.tolvenrise.co.uk/
http://www.qpwd.org.uk/
http://www.wendrowkeyplot.co.uk/
http://www.ruvasto.co.uk/ (very bad design but looks corporate)
http://www.pellarwatt.org.uk/
http://www.vq.co.uk/ (looks corporate but too busy and boring)
http://www.quellisto.co.uk/business/index.htm
http://www.dormavel.com/
https://www.ostrevan.com/en/index.html
The site is for 4 different audiences:
Consumers | Businesses | Public Sector | Installers
Therefore, it's important that there is some form of way of splitting the site up into these sections (almost like 4 websites in 1). Each section will then have the navigation menu with 7 links.
I've attached our logo (company-logo.jpg) and another logo design we have to display inline with regulations (blue-pact-logo.jpg).
Happy designing, and thank you!

```html
<!DOCTYPE html>
<html lang="en">
<head>
<meta charset="utf-8">
<title>Verdallo Energy</title>
<link href="https://fonts.googleapis.com/css2?family=Source+Sans+3:wght@200;300;400;600;700&family=Open+Sans:wght@400;600;700&family=Arimo:wght@400&display=swap" rel="stylesheet">
<style>
:root{
  --green-dark:#5b8c2a;
  --green-mid:#6aa51e;
  --green-light:#8dc63f;
  --ink:#2b2b2b;
  --text:#3d3d3d;
  --band:#f7f7f7;
  --line:#e2e2e2;
  --footer-top:#4a4a4a;
  --footer-bottom:#646464;
  --footer-text:#b9b9b9;
  --icon-grey:#4d4d4d;
}
*{box-sizing:border-box;margin:0;padding:0}
html,body{width:1122px;height:1200px;overflow:hidden;background:#fff}
body{position:relative;font-family:"Open Sans",sans-serif;color:var(--text)}
.abs{position:absolute}

/* header */
.brand{left:95px;top:30px;display:flex;align-items:center;gap:10px}
.brand-mark{width:44px;height:44px;border-radius:50%;background:var(--green-mid)}
.brand-name{font-family:"Source Sans 3",sans-serif;font-weight:600;font-size:34px;color:var(--green-mid);letter-spacing:.5px}
.social{right:100px;top:25px;display:flex;gap:6px}
.social span{width:26px;height:26px;border-radius:50%;background:var(--icon-grey);display:block}

/* navigation */
.nav{left:95px;top:106px;width:932px;height:39px;border-radius:3px;overflow:hidden;display:flex}
.nav-links{display:flex;background:var(--green-dark);width:672px;list-style:none}
.nav-links li{font-family:"Source Sans 3",sans-serif;font-weight:600;font-size:13.5px;color:#fff;display:flex;align-items:center;justify-content:center;border-right:1px solid #4b7722}
.nav-links li:last-child{border-right:none}
.search{flex:1;background:var(--green-light);position:relative}
.search-input{position:absolute;left:23px;top:8px;width:185px;height:22px;background:#fff;border:1px solid #d6e8bf}
.search-go{position:absolute;left:214px;top:8px;width:29px;height:22px;background:var(--green-dark);color:#fff;font-family:"Source Sans 3",sans-serif;font-weight:700;font-size:13px;display:flex;align-items:center;justify-content:center}

/* hero */
.hero-art{left:262px;top:158px;width:598px;height:353px;background:radial-gradient(ellipse at 50% 55%,#e9c2ad 0%,#f3dcd0 35%,#fbf3ef 60%,#fff 80%)}
.hero-dots{left:868px;top:476px;display:flex;gap:9px}
.hero-dots span{width:13px;height:13px;border-radius:50%;background:linear-gradient(#d9d9d9,#a9a9a9);border:1px solid #9a9a9a}
.hero-dots span.active{background:#f3f3f3}

/* welcome band */
.welcome-band{left:0;top:511px;width:1122px;height:249px;background:var(--band)}
.welcome-title{left:98px;top:534px;font-family:"Source Sans 3",sans-serif;font-weight:600;font-size:25px;color:var(--ink)}
.welcome-title em{font-style:normal;color:var(--green-mid)}
.welcome-photo{left:96px;top:577px;width:122px;height:122px;border-radius:50%;border:3px solid #fff;box-shadow:0 0 4px rgba(0,0,0,.25);background:linear-gradient(#3c5670 0%,#7f94a3 45%,#c9b34a 62%,#8d8a2a 100%)}
.welcome-copy{left:232px;top:585px;width:528px;font-family:Arimo,sans-serif;font-size:13px;line-height:20.6px;color:#333}

.consumer-box{left:776px;top:548px;width:251px;height:163px;background:#fff;box-shadow:0 6px 8px -6px rgba(0,0,0,.18)}
.consumer-box h2{position:absolute;left:16px;top:9px;font-family:"Source Sans 3",sans-serif;font-weight:400;font-size:24px;color:#4a4a4a}
.consumer-box h2 em{font-style:normal;color:var(--green-mid);font-weight:600}
.consumer-box ul{position:absolute;left:10px;top:47px;list-style:none}
.consumer-box li{font-family:Arimo,sans-serif;font-size:13px;line-height:22.5px;color:#555;padding-left:13px;position:relative}
.consumer-box li::before{content:"";position:absolute;left:0;top:8px;border-left:6px solid var(--green-mid);border-top:3px solid transparent;border-bottom:3px solid transparent}

/* news */
.news-icon{left:101px;top:792px;width:42px;height:40px;border-radius:6px;background:linear-gradient(135deg,#9ad04a,#4f8d1d)}
.news-title{left:157px;top:795px;font-family:"Source Sans 3",sans-serif;font-weight:600;font-size:25px;color:var(--ink)}
.news-title em{font-style:normal;font-weight:400;color:var(--green-mid)}
.news-list{left:101px;top:846px;list-style:none;width:310px}
.news-list li{position:relative;padding-left:21px;margin-bottom:18px}
.news-list li::before{content:"";position:absolute;left:2px;top:5px;width:11px;height:11px;border-radius:50%;background:var(--green-mid)}
.news-list h3{font-size:13px;font-weight:700;color:var(--green-mid);line-height:20px}
.news-list p{font-size:12px;line-height:19.5px;color:#2e2e2e}
.divider{left:423px;top:785px;width:1px;height:272px;background:linear-gradient(#fff,var(--line) 20%,var(--line) 80%,#fff)}

.card{top:797px;width:171px;height:250px;border:1px solid #e3e3e3;border-radius:3px;background:#fafafa}
.card::after{content:"";position:absolute;left:14px;right:14px;bottom:-8px;height:8px;border-radius:50%;background:radial-gradient(ellipse at 50% 0,rgba(0,0,0,.16),rgba(0,0,0,0) 70%)}
.card h3{text-align:center;margin-top:11px;font-family:"Source Sans 3",sans-serif;font-weight:600;font-size:20px;color:var(--ink);height:28px}
.card-photo{display:block;margin:0 9px;height:73px}
.card p{padding:11px 10px 0 11px;font-size:11px;line-height:16.8px;color:#333}
.card-public{left:451px}
.card-installers{left:654px}
.card-business{left:855px}
.photo-office{background:linear-gradient(90deg,#5a6f8a,#dde3e8 55%,#2b2b30)}
.photo-desk{background:linear-gradient(160deg,#2a2d33,#8f959c 55%,#e6e7e9)}
.photo-team{background:linear-gradient(90deg,#e9ecef,#2d3340 35%,#dfe2e6 65%,#2b2f3a)}

/* footer */
.footer{left:0;top:1089px;width:1122px;height:111px;background:linear-gradient(var(--footer-top),var(--footer-bottom))}
.footer-brand{left:95px;top:1113px;display:flex;align-items:center;gap:9px}
.footer-brand .brand-mark{width:42px;height:42px;background:#c9c9c9}
.footer-brand .brand-name{color:#cfcfcf;font-size:32px}
.talk{left:411px;top:1104px;display:flex;align-items:center;gap:12px;font-family:"Source Sans 3",sans-serif;color:var(--footer-text)}
.talk-label{font-weight:300;font-size:20px}
.talk-number{font-weight:200;font-size:40px;letter-spacing:-.5px}
.footer-rule{left:411px;top:1150px;width:338px;border-top:1px dotted #7d7d7d}
.legal{left:417px;top:1166px;font-family:"Source Sans 3",sans-serif;font-size:12px;color:#9d9d9d;letter-spacing:.3px}
.footer-social{left:880px;top:1109px;display:flex;gap:5px}
.footer-social span{width:30px;height:30px;border-radius:50%;background:#a4a4a4;display:block}
</style>
</head>
<body>

<header>
  <div class="abs brand"><span class="brand-mark"></span><span class="brand-name">Verdallo Energy</span></div>
  <div class="abs social" aria-label="Social links"><span></span><span></span><span></span></div>
  <nav class="abs nav">
    <ul class="nav-links">
      <li style="width:86px">HOME</li>
      <li style="width:112px">ABOUT US</li>
      <li style="width:100px">ENERGY</li>
      <li style="width:129px">WHAT WE DO</li>
      <li style="width:88px">NEWS</li>
      <li style="width:157px">CONTACT US</li>
    </ul>
    <div class="search"><span class="search-input"></span><span class="search-go">GO</span></div>
  </nav>
</header>

<section>
  <div class="abs hero-art" role="img" aria-label="Two cupped hands around a young tree growing from a mound of soil"></div>
  <div class="abs hero-dots"><span></span><span class="active"></span><span></span><span></span><span></span></div>
</section>

<section>
  <div class="abs welcome-band"></div>
  <h1 class="abs welcome-title">Welcome to <em>Verdallo Energy</em></h1>
  <div class="abs welcome-photo" role="img" aria-label="Farmhouse in a yellow field under a stormy sky"></div>
  <p class="abs welcome-copy">Lorem Ipsum is simply dummy text of the printing and typesetting industry. Lorem Ipsum has been the industry's standard dummy text ever since the 1500s, when an unknown printer took a galley of type and scrambled it to make a type specimen book.Lorem Ipsum has been the industry's standard dummy text ever since the 1500s, when an unknown printer took a galley of type and scrambled it to make a type specimen book.</p>
  <aside class="abs consumer-box">
    <h2>Consumers <em>Energy</em></h2>
    <ul>
      <li>simply dummy text of the printing</li>
      <li>when an unknown printer took</li>
      <li>standard dummy text ever</li>
      <li>the printing and typesetting industry.</li>
    </ul>
  </aside>
</section>

<section>
  <div class="abs news-icon" role="img" aria-label="Green news feed illustration"></div>
  <h2 class="abs news-title">Latest <em>News</em></h2>
  <ul class="abs news-list">
    <li><h3>Impact of the Carbon Price &amp; Carbon</h3><p>Thursday 10 November - Afternoon Conference.<br>Registration fee includes lunch.</p></li>
    <li><h3>Impact of the Carbon Price &amp; Carbon</h3><p>Thursday 10 November - Afternoon Conference.<br>Registration fee includes lunch.</p></li>
    <li><h3>Impact of the Carbon Price &amp; Carbon</h3><p>Thursday 10 November - Afternoon Conference.<br>Registration fee includes lunch.</p></li>
  </ul>
  <div class="abs divider"></div>

  <article class="abs card card-public">
    <h3>Public Sector</h3>
    <span class="card-photo photo-office" role="img" aria-label="Office worker at a computer desk"></span>
    <p>simply dummy text of the printing and typesetting industry. Lorem Ipsum has been the industry's standard when an un known printer took a galley</p>
  </article>
  <article class="abs card card-installers">
    <h3>Installers</h3>
    <span class="card-photo photo-desk" role="img" aria-label="Hand stamping a document beside a laptop"></span>
    <p>simply dummy text of the printing and typesetting industry. Lorem Ipsum has been the industry's standard when an un known printer took a galley</p>
  </article>
  <article class="abs card card-business">
    <h3>Businesses</h3>
    <span class="card-photo photo-team" role="img" aria-label="Business team gathered around a meeting table"></span>
    <p>simply dummy text of the printing and typesetting industry. Lorem Ipsum has been the industry's standard when an un known printer took a galley</p>
  </article>
</section>

<footer>
  <div class="abs footer"></div>
  <div class="abs footer-brand"><span class="brand-mark"></span><span class="brand-name">Verdallo Energy</span></div>
  <div class="abs talk">
    <span class="talk-label">Talk to us!</span>
    <svg width="14" height="26" viewBox="0 0 14 26" aria-hidden="true"><path d="M4 1h4l1 6-3 2c0 3 1 6 2 8l3-1 2 6-3 3C5 25 1 17 1 9 1 5 2 2 4 1z" fill="#b9b9b9"/></svg>
    <span class="talk-number">800 314 276</span>
  </div>
  <div class="abs footer-rule"></div>
  <p class="abs legal">©2013 . All rights reserved. &nbsp; Privacy Policy &nbsp;| &nbsp;Terms &amp; Conditions</p>
  <div class="abs footer-social" aria-label="Social links"><span></span><span></span><span></span><span></span></div>
</footer>

</body>
</html>
```